BOLD Gym Needs a New WALL WRAP!

We have a small wall that we need to spice up and we'd like to wrap it with a bold design that stands out and breaks up the current bland grey color.
The wall itself is 128.25" long x 50.5" tall
I am open to design options, but the design must include our PulvaRex logo (attached)
I have also included photos of the gym to give you an idea of the vibe, colors, etc.
DO NOT BE AFRAID OF COLOR😊​ Although our colors are Yellow, Grey's, Blacks, etc., in the gym, please do not be afraid to play with color while still making it look like it belongs in our building. The posters that hang around that wall have pinks, purples, etc. in it. I've included a poster for you to see the colors that are nearby.
The photo from the ground looking up towards the second story highlights the wall that needs to be wrapped.
The ultimate goal here is to break up the grey wall with a killer design.

```html
<!DOCTYPE html>
<html lang="en">
<head>
<meta charset="utf-8">
<title>PulvaRex Wall Wrap</title>
<link rel="stylesheet" href="https://fonts.googleapis.com/css2?family=Permanent+Marker&display=swap">
<style>
  :root {
    --page: #ffffff;
    --yellow: #f7e200;
    --red: #f23a1c;
    --orange: #f46a14;
    --rust: #b8431a;
    --charcoal: #3a3330;
    --white: #efefef;
  }
  html, body {
    margin: 0;
    padding: 0;
    width: 837px;
    height: 1200px;
    overflow: hidden;
    background: var(--page);
  }
  .canvas {
    position: relative;
    width: 837px;
    height: 1200px;
    display: flex;
    align-items: center;
    justify-content: center;
  }
  .wall-wrap {
    position: relative;
    width: 837px;
    height: 332px;
    overflow: hidden;
    background: var(--yellow);
  }
  .wall-wrap__stripes {
    position: absolute;
    inset: 0;
    width: 100%;
    height: 100%;
  }
  .brand {
    position: absolute;
    left: 0;
    right: 0;
    top: 46px;
    text-align: center;
    font-family: "Permanent Marker", cursive;
    font-size: 30px;
    line-height: 1;
    color: var(--yellow);
    margin: 0;
  }
  .headline {
    position: absolute;
    left: 0;
    right: 0;
    top: 80px;
    margin: 0;
    font-family: "Permanent Marker", cursive;
    font-weight: 400;
    color: var(--white);
    text-align: center;
    transform: rotate(-4deg);
    line-height: 0.95;
    letter-spacing: -1px;
    text-shadow:
      -3px -3px 0 var(--charcoal), 3px -3px 0 var(--charcoal),
      -3px 3px 0 var(--charcoal), 3px 3px 0 var(--charcoal),
      5px 6px 0 var(--charcoal), 7px 9px 0 var(--charcoal),
      9px 12px 0 var(--charcoal), 11px 14px 0 var(--charcoal);
  }
  .headline__line {
    display: block;
  }
  .headline__line--top {
    font-size: 104px;
    padding-left: 40px;
  }
  .headline__line--bottom {
    font-size: 108px;
    padding-right: 10px;
  }
</style>
</head>
<body>
  <main class="canvas">
    <section class="wall-wrap">
      <svg class="wall-wrap__stripes" viewBox="0 0 837 332" preserveAspectRatio="none" aria-hidden="true">
        <!-- left diagonal bands -->
        <polygon points="0,40 40,0 95,0 0,110" fill="var(--red)"/>
        <polygon points="0,150 120,0 175,0 0,230" fill="var(--red)"/>
        <polygon points="75,50 125,0 145,0 90,70" fill="var(--charcoal)"/>
        <polygon points="0,332 0,280 210,40 260,60 60,332" fill="var(--red)"/>
        <polygon points="120,332 300,120 330,150 170,332" fill="var(--orange)"/>
        <polygon points="140,90 230,60 260,80 170,130" fill="var(--rust)" opacity="0.8"/>
        <!-- right diagonal bands -->
        <polygon points="560,0 700,0 640,70 540,60" fill="var(--rust)" opacity="0.85"/>
        <polygon points="690,0 760,0 690,90 640,80" fill="var(--orange)"/>
        <polygon points="770,0 837,0 837,20 710,180 660,170" fill="var(--red)"/>
        <polygon points="837,60 837,130 700,310 640,300" fill="var(--red)"/>
        <polygon points="837,170 837,220 740,332 700,332" fill="var(--rust)"/>
        <polygon points="600,332 700,210 740,220 650,332" fill="var(--red)"/>
        <polygon points="520,332 560,280 600,290 570,332" fill="var(--charcoal)"/>
        <polygon points="500,250 620,230 680,270 560,300" fill="var(--orange)" opacity="0.9"/>
        <polygon points="0,180 110,200 80,250 0,240" fill="var(--orange)" opacity="0.9"/>
        <!-- dark band behind brand name -->
        <path d="M318,40 Q418,24 500,34 L500,82 Q410,88 318,80 Z" fill="var(--charcoal)"/>
      </svg>
      <p class="brand">PulvaRex</p>
      <h1 class="headline">
        <span class="headline__line headline__line--top">YOUR ONLY</span>
        <span class="headline__line headline__line--bottom">LIMIT IS YOU</span>
      </h1>
    </section>
  </main>
</body>
</html>
```